BW Law Firm Needs Sharp Letterhead

Our law firm recently selected a new logo through Pixelfair. Now we need a sharp Letterhead using the Letterhead.

Target Market(s)

Legal community, business clients

Industry/Entity Type

Law Firm

Requirements
Must have
• Our Logo
• Gordon P. Ashby
• Board Certified
• Civil Trial Law
• Ohio Council of Counsel Accreditation
• gashby@bwlegalteam.com
• 2715-C West 6th
• McAllen, TX 78599
• 555-213-0476
• www.bwlegalteam.com

```html
<!DOCTYPE html>
<html lang="en">
<head>
<meta charset="utf-8">
<title>BW Law Firm – Letterhead</title>
<link rel="stylesheet" href="https://fonts.googleapis.com/css2?family=Cinzel:wght@400;500&family=Libre+Baskerville&display=swap">
<style>
  :root {
    --canvas: #ececec;
    --paper: #ffffff;
    --frame-line: #9a9b9d;
    --band-dark: #6f7072;
    --band-light: #c3c4c6;
    --band-lighter: #d4d5d7;
    --ink: #1f1f1f;
    --tagline: #7d8c86;
    --accent: #c4161c;
  }
  * { margin: 0; padding: 0; box-sizing: border-box; }
  html, body {
    width: 1200px;
    height: 900px;
    overflow: hidden;
    background: var(--canvas);
  }
  .letterhead {
    position: absolute;
    left: 308px;
    top: 40px;
    width: 577px;
    height: 817px;
    background: var(--paper);
  }
  .letterhead svg { display: block; }
  .firm-name {
    font-family: "Cinzel", serif;
    font-weight: 500;
    font-size: 21px;
    fill: var(--ink);
    letter-spacing: 0.3px;
  }
  .firm-tagline {
    font-family: "Cinzel", serif;
    font-size: 8px;
    fill: var(--tagline);
    letter-spacing: 0.4px;
  }
  .web-address {
    font-family: "Libre Baskerville", serif;
    font-size: 12.5px;
    fill: var(--ink);
  }
</style>
</head>
<body>
  <div class="letterhead">
    <svg width="577" height="817" viewBox="0 0 577 817" xmlns="http://www.w3.org/2000/svg">
      <defs>
        <linearGradient id="footer-pill-fill" x1="0" x2="1" y1="0" y2="0">
          <stop offset="0" stop-color="#c3c4c6"/>
          <stop offset="0.45" stop-color="#ffffff"/>
          <stop offset="1" stop-color="#ffffff"/>
        </linearGradient>
      </defs>

      <!-- side bands -->
      <polygon class="band-dark" points="0,230 22,244 22,310 0,298" fill="var(--band-dark)"/>
      <polygon class="band-light" points="0,298 577,495 577,817 0,817" fill="var(--band-light)"/>
      <polygon class="band-lighter" points="555,487 577,495 577,572 555,562" fill="var(--band-lighter)"/>

      <!-- writing area frame -->
      <rect class="writing-area" x="22" y="50" width="533" height="717" rx="14" fill="var(--paper)"/>
      <path class="frame-line" d="M54,50 H36 A14,14 0 0 0 22,64 V753 A14,14 0 0 0 36,767 H541 A14,14 0 0 0 555,753 V64 A14,14 0 0 0 541,50 H338"
            fill="none" stroke="var(--frame-line)" stroke-width="0.8"/>

      <!-- firm name block -->
      <rect class="firm-mark" x="66" y="35" width="26" height="30" fill="var(--ink)"/>
      <text class="firm-name" x="100" y="54">Brightwell Wade</text>
      <line class="firm-rule" x1="100" y1="57" x2="306" y2="57" stroke="var(--frame-line)" stroke-width="0.6"/>
      <text class="firm-tagline" x="100" y="66">Attorneys and Counselors</text>

      <!-- footer web address -->
      <rect class="footer-pill" x="232" y="777" width="323" height="21" rx="10.5" fill="url(#footer-pill-fill)"/>
      <rect class="footer-accent" x="395" y="783" width="9" height="9" fill="var(--accent)"/>
      <text class="web-address" x="408" y="792">www.bwlegalteam.com</text>
    </svg>
  </div>
</body>
</html>
```